Decorative concrete business needs new business cards

Our company attracts homeowners and business with disposable cash. We are a artistic decorative coatings company that will transform your driveway, patio, floors or counter tops into a work of art. We also engrave logos and designs right into the concrete! We are upscale and very professional company. I am open for rearranging our logo on the business card and also to different color patterns. We like the blue and black as in BrushNest's logo. We also like blue and orange/yellow.

Target Market(s)

Adults 30-70

Industry/Entity Type

Concrete

Contact Information for Business Card

Simple: Name, phone, email, website and social media icons

Font styles to use
Serif

Colors

Designer to choose colors to be used in the design.

Requirements
Must have
• Must present a professional upscale appearance. I have attached before and after photos that show you what our industry does. Maybe I will have before and after photo on back of card.
Nice to have
• Artistic, but bold. Nothing whimsical or cute.
Should not have
• Should not have cartoon or childlike appearance.

```html
<!DOCTYPE html>
<html lang="en">
<head>
<meta charset="utf-8">
<title>Stonecraft Finish Works – Business Cards</title>
<link rel="stylesheet" href="https://fonts.googleapis.com/css2?family=Cinzel:wght@600&family=Montserrat:wght@400;500;600&display=swap">
<style>
  :root {
    --stage: #2e2e2e;
    --card-dark: #050505;
    --card-light: #ffffff;
    --brand-blue: #2a8fc9;
    --brand-orange: #ef9a1e;
    --text-grey: #6d6d6d;
    --rule-grey: #b5b5b5;
    --white: #ffffff;
  }
  * { margin: 0; padding: 0; box-sizing: border-box; }
  html, body {
    width: 1200px; height: 864px; overflow: hidden;
    background: var(--stage);
  }
  .stage {
    width: 1200px; height: 864px;
    display: flex; flex-direction: column;
    align-items: center; justify-content: center; gap: 36px;
  }
  .card {
    width: 620px; height: 354px;
    position: relative;
    box-shadow: 0 8px 24px rgba(0,0,0,.45);
  }
  .card--back {
    background: var(--card-dark);
    display: flex; flex-direction: column; align-items: center; justify-content: center;
  }
  .card--front {
    background: var(--card-light);
    display: flex; align-items: center;
    padding: 0 40px 0 52px;
  }
  .brand {
    display: flex; align-items: center; gap: 14px;
  }
  .brand__mark {
    width: 22px; height: 22px;
    background: var(--brand-orange);
    flex: none;
  }
  .brand__name {
    font-family: "Cinzel", serif;
    font-weight: 600;
    color: var(--brand-blue);
    font-size: 30px;
    line-height: 1.05;
    letter-spacing: 1px;
  }
  .card--back .brand__name { font-size: 34px; }
  .card--back .brand__mark { width: 26px; height: 26px; }
  .back__website {
    margin-top: 64px;
    font-family: "Montserrat", sans-serif;
    font-size: 14px;
    color: var(--white);
    letter-spacing: .3px;
  }
  .front__divider {
    width: 1px; height: 150px;
    background: var(--rule-grey);
    margin: 0 28px;
    flex: none;
  }
  .contact__name {
    font-family: "Montserrat", sans-serif;
    font-weight: 600;
    font-size: 21px;
    color: var(--brand-blue);
  }
  .contact__role {
    font-family: "Montserrat", sans-serif;
    font-size: 14px;
    color: var(--text-grey);
    margin: 2px 0 18px;
  }
  .contact__list { list-style: none; }
  .contact__item {
    display: flex; align-items: center; gap: 8px;
    font-family: "Montserrat", sans-serif;
    font-size: 13.5px;
    color: var(--text-grey);
    line-height: 1.6;
  }
  .contact__icon { width: 13px; height: 13px; flex: none; }
</style>
</head>
<body>
<main class="stage">
  <section class="card card--back" aria-label="Card back">
    <div class="brand">
      <span class="brand__mark"></span>
      <span class="brand__name">Stonecraft<br>Finish Works</span>
    </div>
    <p class="back__website">www.stonecraftfinish.com</p>
  </section>

  <section class="card card--front" aria-label="Card front">
    <div class="brand">
      <span class="brand__mark"></span>
      <span class="brand__name">Stonecraft<br>Finish Works</span>
    </div>
    <div class="front__divider"></div>
    <div class="contact">
      <p class="contact__name">Daniel Reyes</p>
      <p class="contact__role">President</p>
      <ul class="contact__list">
        <li class="contact__item">
          <svg class="contact__icon" viewBox="0 0 16 16"><path d="M4 1l3 3-2 2c1 2 3 4 5 5l2-2 3 3-2 3C7 15 1 9 1 3z" fill="var(--brand-orange)"/></svg>
          555-210-4478
        </li>
        <li class="contact__item">
          <svg class="contact__icon" viewBox="0 0 16 16"><rect x="4" y="1" width="8" height="14" rx="1.5" fill="none" stroke="var(--brand-orange)" stroke-width="1.6"/><circle cx="8" cy="12.5" r="0.9" fill="var(--brand-orange)"/></svg>
          555-210-4479
        </li>
        <li class="contact__item">
          <svg class="contact__icon" viewBox="0 0 16 16"><rect x="1" y="3" width="14" height="10" fill="var(--brand-orange)"/><path d="M1 3l7 6 7-6" fill="none" stroke="#fff" stroke-width="1.3"/></svg>
          info@stonecraftfinish.com
        </li>
        <li class="contact__item">
          <svg class="contact__icon" viewBox="0 0 16 16"><g fill="none" stroke="var(--brand-orange)" stroke-width="1.4"><circle cx="8" cy="8" r="6.5"/><ellipse cx="8" cy="8" rx="3" ry="6.5"/><path d="M1.5 8h13M2.5 4.5h11M2.5 11.5h11"/></g></svg>
          www.stonecraftfinish.com
        </li>
      </ul>
    </div>
  </section>
</main>
</body>
</html>
```